Seeking Talented PSD Designer for Real Estate Finance Web Site

Hello ...
Need a minimalist design for a high - end finance web site that conveys prestige / sophistication / class ... Below are comps for this project ...
http://www.tawnyridgefunding.com/
http://glenmoorfunds.com/
http://www.cedarloftfp.com/
http://halvornfunds.com/
Look forward too receiving proposals for this project ....
Target Market(s)
Commerciale entities seeking more than $500.0 k in interim capital ... These could include apartment owners / construction managers / restaurant owners / hotels / golf courses ...
Industry/Entity Type
Real Estate
Number of Pages Required
1 page
Requirements
Must have
- Super high quality graphic design ... Has to be marketable and convert customers to contact us ...
- Please refer to logo concept four ....
Should not have
- clunky / poor fonts /

```html
<!DOCTYPE html>
<html lang="en">
<head>
<meta charset="utf-8">
<title>Brookvale Capital — Real Estate Finance</title>
<link href="https://fonts.googleapis.com/css2?family=Oswald:wght@400;500&family=Roboto:wght@300;400;500&display=swap" rel="stylesheet">
<style>
:root{
  --navy:#2b3d6b;
  --blue:#2f6db5;
  --accent:#2f6db5;
  --ink:#2a2a2a;
  --muted:#8a8a8a;
  --page:#f7f7f8;
  --black:#151515;
  --white:#ffffff;
  --badge:#cfd2d6;
}
*{box-sizing:border-box;margin:0;padding:0}
html,body{width:1200px;height:2187px;overflow:hidden}
body{font-family:'Roboto',sans-serif;background:var(--page);color:var(--ink);position:relative}

/* header */
.header{position:absolute;left:0;top:0;width:1200px;height:170px;background:var(--page)}
.brand{position:absolute;left:88px;top:60px;display:flex;align-items:center;gap:12px}
.brand-dot{width:34px;height:34px;border-radius:50%;background:var(--navy)}
.brand-name{font-size:25px;font-weight:500;color:var(--navy);line-height:1}
.phone{position:absolute;left:786px;top:42px;font-size:21px;color:var(--ink);display:flex;align-items:center;gap:10px}
.social{position:absolute;left:972px;top:40px;display:flex;gap:7px}
.social span{width:28px;height:28px;border-radius:50%;background:var(--navy)}
.social span:nth-child(2){background:#c9463d}
.social span:nth-child(3){background:#2d9ad8}
.social span:nth-child(4){background:#e8641c}
.nav{position:absolute;left:328px;top:110px;width:872px;height:60px;background:var(--navy);clip-path:polygon(36px 0,100% 0,100% 100%,0 100%)}
.nav ul{list-style:none;display:flex;position:absolute;left:60px;top:0;height:60px;align-items:center}
.nav li{color:var(--white);font-size:15px;margin-right:38px}

/* hero */
.hero{position:absolute;left:0;top:170px;width:1200px;height:533px;background:linear-gradient(180deg,#59606c 0%,#3b4250 35%,#262a33 70%,#1c1f26 100%)}
.hero-title{position:absolute;left:122px;top:310px;font-family:'Oswald',sans-serif;font-size:51px;line-height:1.1;color:var(--white);font-weight:400}
.hero-sub{position:absolute;left:123px;top:375px;font-size:22px;line-height:1.2;color:var(--white);font-weight:400}
.hero-arrows{position:absolute;left:1037px;top:484px;display:flex}
.hero-arrows span{width:29px;height:29px;display:flex;align-items:center;justify-content:center}
.arrow-prev{background:var(--white)}
.arrow-next{background:var(--blue)}

/* welcome */
.welcome-title{position:absolute;left:0;top:746px;width:1200px;text-align:center;font-size:22px;font-weight:400;color:var(--ink)}
.welcome-title em{font-style:normal;color:var(--accent)}
.welcome-text{position:absolute;left:86px;top:792px;width:1028px;text-align:center;font-size:12px;line-height:22px;color:var(--muted)}

.service{position:absolute;top:934px;width:330px}
.service-icon{position:absolute;left:0;top:0;width:93px;height:93px;border:1px solid var(--navy);border-radius:50%;display:flex;align-items:center;justify-content:center}
.service h3{position:absolute;left:116px;top:2px;font-size:16px;font-weight:400;white-space:nowrap;color:var(--ink)}
.service p{position:absolute;left:116px;top:34px;width:200px;font-size:11.5px;line-height:21px;color:var(--muted)}

/* features band */
.features{position:absolute;left:0;top:1095px;width:1200px;height:298px;background:linear-gradient(90deg,#3f4c6e,#4a5a80)}
.features-img{position:absolute;left:530px;top:0;width:670px;height:298px;background:linear-gradient(135deg,#e6e7ea 0%,#b7c1cf 35%,#4d6080 65%,#2e3f5c 100%);clip-path:polygon(115px 0,100% 0,100% 100%,0 100%)}
.features h2{position:absolute;left:88px;top:42px;font-size:24px;font-weight:400;color:var(--white)}
.features ul{position:absolute;left:86px;top:87px;list-style:none}
.features li{font-size:14px;color:var(--white);line-height:28.3px;font-weight:300}
.features li::before{content:"»";margin-right:7px}

/* projects */
.projects-head{position:absolute;left:0;top:1393px;width:1200px;height:100px;background:linear-gradient(180deg,#1d2230,#2a3040)}
.projects-head h2{position:absolute;left:0;top:38px;width:1200px;text-align:center;font-size:24px;font-weight:400;color:var(--white)}
.project{position:absolute;top:1493px;width:300px;height:283px}
.p1{left:0;background:linear-gradient(180deg,#2f4fb8,#56668c 60%,#2e3540)}
.p2{left:302px;background:linear-gradient(180deg,#3f5fc0,#d7dbe4 55%,#6e7468)}
.p3{left:604px;background:linear-gradient(180deg,#d7e3f3,#3b7dd0 55%,#b58a5c)}
.p4{left:906px;width:294px;background:linear-gradient(180deg,#6f9fd8,#a89278 55%,#4f7a32)}
.proj-arrow{position:absolute;top:1626px;width:20px;height:20px;border-radius:50%;background:rgba(255,255,255,.55)}

/* partners */
.partners{position:absolute;left:66px;top:1800px;width:1080px;height:66px;background:var(--white);display:flex;justify-content:space-around;align-items:center;padding:0 30px}
.partner{width:130px;height:28px;border-radius:4px;background:var(--badge)}

/* footer */
.footer{position:absolute;left:0;top:1885px;width:1200px;height:222px;background:var(--blue);color:var(--white)}
.fcol{position:absolute;top:40px}
.fcol h4{font-size:15px;font-weight:400;margin-bottom:22px}
.links{list-style:none}
.links li{font-size:11px;line-height:24.5px}
.links li::before{content:"›";margin-right:6px}
.fcol p{font-size:10.5px;line-height:16px}
.newsletter-form{display:flex;margin-top:18px}
.newsletter-form span{display:block;height:31px;line-height:31px;font-size:10px}
.nf-input{width:146px;background:var(--white);color:#777;padding-left:13px}
.nf-btn{width:55px;background:var(--black);color:var(--white);text-align:center;font-size:12px}
.fsocial{display:flex;gap:15px;margin-top:17px}
.fsocial span{width:33px;height:33px;border:1px solid var(--white);border-radius:50%}

.copyright{position:absolute;left:0;top:2107px;width:1200px;height:80px;background:var(--black);color:var(--white);font-size:12px}
.copyright p{position:absolute;left:0;top:37px;width:1200px;text-align:center}
.copyright .code{position:absolute;left:1160px;top:37px;font-size:12px}
</style>
</head>
<body>

<header class="header">
  <div class="brand">
    <span class="brand-dot"></span>
    <span class="brand-name">Brookvale Capital</span>
  </div>
  <div class="phone">
    <svg width="17" height="17" viewBox="0 0 24 24"><rect width="24" height="24" rx="4" fill="#2b3d6b"/><path d="M8 5l2.5 3-1.5 2c1 2 2.5 3.5 4.5 4.5l2-1.5 3 2.5-1.5 2.5C12 18 6 12 5.5 6.5z" fill="#fff"/></svg>
    310.555.0142
  </div>
  <div class="social" aria-label="Social links"><span></span><span></span><span></span><span></span></div>
  <nav class="nav">
    <ul><li>HOME</li><li>ABOUT US</li><li>SERVICES</li><li>PROPERTIES</li><li>INVESTMENT</li><li>NEWS</li><li>CONTACTS</li></ul>
  </nav>
</header>

<section class="hero" role="img" aria-label="Aerial view of a city skyline at dusk with towers and lights">
  <h1 class="hero-title">REAL ESTATE FINANCE</h1>
  <p class="hero-sub">Neque porro quisquam est qui dolorem</p>
  <div class="hero-arrows">
    <span class="arrow-prev"><svg width="10" height="10" viewBox="0 0 10 10"><path d="M6.5 1.5L3 5l3.5 3.5" stroke="#222" stroke-width="1.6" fill="none"/></svg></span>
    <span class="arrow-next"><svg width="10" height="10" viewBox="0 0 10 10"><path d="M3.5 1.5L7 5 3.5 8.5" stroke="#fff" stroke-width="1.6" fill="none"/></svg></span>
  </div>
</section>

<h2 class="welcome-title">WELCOME TO <em>BROOKVALE CAPITAL</em></h2>
<p class="welcome-text">Lorem Ipsum has been the industry's standard dummy text ever since the 1500s, when an unknown printer took a galley of type and scrambled it to make a type specimen book. It has survived not only five centuries, but also the leap into electronic typesetting, remaining essentially unchanged. It was popularised in the 1960s with the release of printed transfer sheets containing Lorem Ipsum passages, and more recently with desktop publishing software and modern layout programs including versions of Lorem Ipsum.</p>

<div class="service" style="left:90px">
  <div class="service-icon"><svg width="30" height="42" viewBox="0 0 30 42"><rect width="30" height="42" fill="#2f6db5"/><g fill="#fff"><rect x="5" y="5" width="5" height="4"/><rect x="12.5" y="5" width="5" height="4"/><rect x="20" y="5" width="5" height="4"/><rect x="5" y="13" width="5" height="4"/><rect x="12.5" y="13" width="5" height="4"/><rect x="20" y="13" width="5" height="4"/><rect x="5" y="21" width="5" height="4"/><rect x="12.5" y="21" width="5" height="4"/><rect x="20" y="21" width="5" height="4"/><rect x="11" y="31" width="8" height="11"/></g></svg></div>
  <h3>COMMERCIAL PROPERTIES</h3>
  <p>Lorem ipsum dolor sit amet, coetur adipiscing elit. Vivamus luctus urna sed urna ultricies ac tempor</p>
</div>
<div class="service" style="left:446px">
  <div class="service-icon"><svg width="38" height="34" viewBox="0 0 38 34"><path d="M19 2L2 17h5v15h9v-9h6v9h9V17h5z" fill="#2f6db5"/></svg></div>
  <h3>RESIDENTIAL PROPERTIES</h3>
  <p>Lorem ipsum dolor sit amet, coetur adipiscing elit. Vivamus luctus urna sed urna ultricies ac tempor</p>
</div>
<div class="service" style="left:806px">
  <div class="service-icon"><svg width="42" height="40" viewBox="0 0 42 40"><g fill="#2b3d6b"><circle cx="15" cy="23" r="11"/><circle cx="31" cy="11" r="8"/></g><circle cx="15" cy="23" r="4.5" fill="#fff"/><circle cx="31" cy="11" r="3" fill="#fff"/></svg></div>
  <h3>BUSINESS</h3>
  <p>Lorem ipsum dolor sit amet, coetur adipiscing elit. Vivamus luctus urna sed urna ultricies ac tempor</p>
</div>

<section class="features">
  <div class="features-img" role="img" aria-label="Modern glass office building lit at dusk beside a tower"></div>
  <h2>BROOKVALE CAPITAL FEATURES</h2>
  <ul>
    <li>Neque porro quisquam est qui dolorem ipsum quia dolor sit amet</li>
    <li>Lorem Ipsum is simply dummy text of the printing</li>
    <li>Neque porro quisquam est qui dolorem ipsum quia dolor</li>
    <li>simply dummy text of the printing and typesetting</li>
    <li>Lorem Ipsum passages, and more recently with desktop</li>
    <li>The point of using Lorem Ipsum is that it has a more-or-less</li>
  </ul>
</section>

<section class="projects-head" role="img" aria-label="Dark city skyline backdrop"><h2>OUR PROJECTS</h2></section>
<div class="project p1" role="img" aria-label="Modern apartment block at dusk"></div>
<div class="project p2" role="img" aria-label="White contemporary house with palm"></div>
<div class="project p3" role="img" aria-label="Glass office towers seen from below"></div>
<div class="project p4" role="img" aria-label="Suburban family home with lawn"></div>
<span class="proj-arrow" style="left:20px"></span>
<span class="proj-arrow" style="left:1158px"></span>

<div class="partners" aria-label="Platform partners">
  <span class="partner"></span><span class="partner"></span><span class="partner"></span><span class="partner"></span><span class="partner"></span>
</div>

<footer class="footer">
  <div class="fcol" style="left:89px">
    <h4>LINKS</h4>
    <ul class="links"><li>Customer Support</li><li>Documentation</li><li>Resources</li><li>General FAQs</li><li>Shortcodes</li></ul>
  </div>
  <div class="fcol" style="left:300px;width:230px">
    <h4>REAL ESTATE FINANCE</h4>
    <p>Lorem Ipsum has been the industry's standard dummy text ever since the 1500s, when an unknown printer took</p>
    <p style="margin-top:8px">a galley of type and scrambled it to make a type specimen book. It has survived not only five centuries, but also the leap into electronic typeset-</p>
  </div>
  <div class="fcol" style="left:651px">
    <h4>GET IN TOUCH</h4>
    <p>Address : 1200 Harbor View Ave,<br>Bayridge, NJ</p>
    <p style="margin-top:14px">Phone : 201 555 0187</p>
    <p style="margin-top:14px">Email : info@brookvalemail.com</p>
  </div>
  <div class="fcol" style="left:907px">
    <h4>NEWSLETTER</h4>
    <p>Your about us information would fit<br>here nicely.</p>
    <div class="newsletter-form"><span class="nf-input">Email address</span><span class="nf-btn">Submit</span></div>
    <div class="fsocial"><span></span><span></span><span></span></div>
  </div>
</footer>

<div class="copyright">
  <p>Copyright © 2016. All Rights Reserved</p>
  <span class="code">C6</span>
</div>

</body>
</html>
```